New web/graphic designs required to improve existing ecommerce site.

Initial outline of project:
This project is for new designs to fit into areas of existing webpages - specifically:-
Objective 1 - Produce 8 home page design proposals (design for central area of page only, not whole page)
Objective 2 - Produce 5 designs for page header banners (950px x 84px images)
Objective 3 - Produce 10 designs for help guide covers (316px x 410px images)
Also, on a more general note:
Objective 4 - Review and suggest improvements for other areas website. (This may lead to further design work)
-
Introduction to the Periodical Bazaar website:
The Periodical Bazaar website is a marketplace where back-issue hobby magazines can be bought and sold, and in some cases downloaded & viewed in digital form. The ‘sellers’ of the magazines will be both traders and private individuals. Trade sellers will also be able to sell magazine subscriptions and have ‘Promotion Pages’ about themselves and/or their magazine titles on the site. Other forms of advertising will also be available on the site for any commercial advertisers who want it, particularly for companies supplying the various hobbies covered.
Users of the website can locate magazines of interest to them by browsing through the hobby / category sections of the site, or by doing keyword searches for issues containing articles on specific topics.
The site is split-up into sections dealing with magazines about specific hobby subjects – ie., cars, motorbikes, railway, aviation, boating etc. Although part of the larger site, each of these sections is largely self-contained, with many users only ever browsing in the section related to their hobby. As such, each section effectively has it’s own home page, which will duplicate much of the information shown on the main home page. These multiple ‘section home pages’ will be promoted in their own right via URLs specific to that hobby. Currently there are 8 sections, but this number is expected to increase as the site grows.
This website is still being developed, but is close to launch; as such the website is fully functional but a lot of content is missing - please bear this in mind when viewing the site, and feel free to ask for clarification if anything is unclear.
The new website is currently at: http://www2.periodicalbazaar.co.uk
This website will replace several existing sites:-
http://www.periodicalbazaar.co.uk
http://www.twowheel-journals.co.uk
http://www.flight-journals.co.uk
http://www.autoreads.co.uk
http://www.trackside-journals.co.uk
http://www.scalecraft-journals.co.uk
-
Design notes:
The overall design is fairly conventional and very much ‘functionality’ driven, the website being at it’s heart an ecommerce system with some fairly complex features. Nevertheless I want the site to appear simple and modern in appearance, being somewhere between an ‘all style’ Web 2.0-type site (eg. quirlo.me), and an ‘all function’ conventional trading site (eg. Vendora, Bidly etc). A good example of a style of site which I would like to emulate is PostGiraffe – a complex and large site made to look friendly and approachable by the use of simple, clear design, bold colour and a sense of humour.
To explain further what is required I have prepared various image documents which include more detailed notes on the various objectives for this project. There is a lot of information in these documents - please read them carefully:-
Objective 1:
- Produce 1 'Main Home Page' design proposal
- Produce 8 'Section Home Page' design proposals - one each for these sections: Railway, Boating, Aviation, Cycling, Automotive, Motorcycling, Men's Lifestyle, Modelling
More information on Objective 1 is given in these image documents:
http://www.filevault-demo.net/Home_Page_Designs-Purpose.gif
http://www.filevault-demo.net/Home_Page_Designs-Areas.gif
http://www.filevault-demo.net/Section_Home_Pages-1.gif
http://www.filevault-demo.net/Section_Home_Pages-2.gif
-
Objective 2:
- Produce 5 designs for page header banners (950px x 84px images)
More information on Objective 2 is given in this image document:
http://www.filevault-demo.net/Page_Header_Banners.gif
-
Objective 3:
- Produce 10 designs for help guide covers (316px x 410px images)
http://www.filevault-demo.net/Help_Guide_Covers.gif
-
Objective 4:
- Review and suggest improvements for other areas website
I would like the designer to spend some time looking at the whole of the current website, and suggest any areas that can be improved. I am not looking for a wholesale re-design - the overall layout of the site and major design elements such as the navigation system - are essentially fixed - however, many graphical elements can be changed, as can any text content (including text content within the navigation system).
Improvements which are suggested may lead to additional design work either as part of this project, or as subsequent projects in their own right.
-
Designers are very welcome to contact me to discuss any aspect of this project, or if more information is required about the website or the designs required.
I'm happy to guarantee this project in due course, if there is positive reaction to the project from potential designers interested in submitting designs. This is the second project I have run on ArtistHive - the first one was successful and resulted in the Flash animation that is currently on the homepage of the website.
UPDATE 11/10/11:
I've created some new documents to illustrate the sort of designs I am looking for for the Main Home Page and Section Home Pages:
Very rough examples of the sort of style I am looking for:
http://www.filevault-demo.net/Rough_Main_Home_Page_1.jpg
http://www.filevault-demo.net/Rough_Main_Home_Page_2.jpg
http://www.filevault-demo.net/Rough_Main_Home_Page_3.jpg
http://www.filevault-demo.net/Rough_Main_Home_Page_4.jpg
http://www.filevault-demo.net/Rough_Main_Home_Page_5.jpg
http://www.filevault-demo.net/Rough_Section_Home_Page.jpg
http://www.filevault-demo.net/Rough_Section_Home_Page_2.jpg
Detailed document showing exact content required for the Main Home Page and each Section Home Page:
http://www.filevault-demo.net/Home_Page_Content.gif
Target Market(s)
Mainly male, age 20 - 60. Not necessarily 'web savvy' or design-conscious
Industry/Entity Type
Advertising
Look and feel
Each slider illustrates characteristics of the customer's brand and the style your logo design should communicate.

```html
<!DOCTYPE html>
<html lang="en">
<head>
<meta charset="utf-8">
<title>Periodical Bazaar – Home</title>
<link href="https://fonts.googleapis.com/css2?family=Open+Sans:ital,wght@0,400;0,600;0,700;1,700&family=Playfair+Display:wght@400&display=swap" rel="stylesheet">
<style>
:root{
  --red:#b3121a;
  --red-dark:#7d0a12;
  --red-bright:#d8232a;
  --orange:#f7a21b;
  --orange-light:#fdc35a;
  --ink:#222;
  --grey-text:#555;
  --panel:#efefef;
  --footer:#2f2f2f;
  --footer-head:#e2262e;
  --blue:#1f6fc0;
}
*{margin:0;padding:0;box-sizing:border-box}
html,body{width:750px;height:1200px;overflow:hidden;background:#fff}
body{position:relative;font-family:"Open Sans",Arial,sans-serif;color:var(--ink)}
.abs{position:absolute}

/* top bar */
.top-bar{left:8px;top:0;width:734px;height:36px;background:linear-gradient(#555,#1c1c1c);border-radius:0 0 8px 8px}
.search-field{left:590px;top:12px;width:101px;height:16px;background:#fff;border-radius:8px;font-size:9px;color:#aaa;text-align:right;padding-right:10px;line-height:16px}
.search-field::before{content:"";position:absolute;left:4px;top:3px;width:8px;height:8px;border:1px solid #999;border-radius:50%}
.go-button{left:704px;top:6px;width:26px;height:26px;border-radius:50%;background:radial-gradient(circle at 40% 35%,#4fa3ee,#0c4f9a);border:2px solid #cfe3f7;color:#fff;font-size:9px;font-weight:700;text-align:center;line-height:22px}

.brand-name{left:22px;top:56px;font-size:17px;font-weight:600;color:var(--ink);letter-spacing:-.2px}
.brand-mark{left:22px;top:79px;width:10px;height:10px;display:none}
.phone-icon{left:566px;top:40px;width:28px;height:28px;border-radius:50%;background:radial-gradient(circle at 40% 35%,#8ed86d,#3c9a2a)}
.phone-number{left:607px;top:42px;font-size:19px;color:#999;letter-spacing:.5px}
.account-links{left:537px;top:80px;font-size:8.5px;color:#222;word-spacing:0}
.account-links span{margin-right:10px}

/* nav */
.main-nav{left:0;top:100px;width:750px;height:28px;background:linear-gradient(#e8323a,#b01018);border-bottom:1px solid #7a0a0f}
.nav-item{top:100px;height:28px;line-height:28px;font-size:11px;color:#fff;text-align:center}
.nav-item.active{left:99px;width:86px;background:linear-gradient(#ffd88a,#f7a21b);color:#5a2a00}

/* hero */
.hero{left:36px;top:130px;width:678px;height:244px;background:radial-gradient(ellipse at 30% 40%,#f9c79a,#f29a4e 60%,#e7802f)}
.hero-shadow{left:30px;top:372px;width:690px;height:8px;background:radial-gradient(ellipse at center,rgba(0,0,0,.25),transparent 70%)}
.hero-title-small{left:65px;top:158px;font-size:30px;color:#fff}
.hero-title-large{left:130px;top:206px;font-size:50px;color:#2a2a2a}
.hero-text{left:76px;top:318px;width:310px;font-size:12.5px;line-height:16px;color:#fff}
.hero-covers{left:395px;top:145px;width:319px;height:229px;background:linear-gradient(135deg,#f4e6dc,#e7a6a0 45%,#d66a8a 70%,#f0d0b0)}
.slide-arrow{top:236px;width:30px;height:42px}

/* welcome */
.section-heading{font-size:16px;font-weight:700;color:var(--red);white-space:nowrap}
.welcome-panel{left:38px;top:414px;width:466px;height:126px;background:linear-gradient(#a31920,#7a0a11);border:1px solid #ccc;box-shadow:0 2px 4px rgba(0,0,0,.25)}
.welcome-intro{left:67px;top:428px;font-size:17px;font-weight:600;color:#fff}
.new-ribbon{left:440px;top:410px;width:66px;height:34px}
.action-button{top:463px;width:101px;height:37px;border-radius:3px;background:linear-gradient(#fbfbf3,#d7d6c3);border:1px solid #999;font-size:16px;font-weight:700;font-style:italic;color:#333;text-align:center;line-height:35px}
.action-button.primary{background:linear-gradient(#ffc04a,#f08a0c);border-color:#c06a00;color:#3a1a00}
.action-caption{top:506px;width:101px;text-align:center;font-size:10px;font-weight:600;color:#fff}

/* article search */
.search-panel{left:33px;top:551px;width:473px;height:75px;background:linear-gradient(#fafafa,#ececec);border:1px solid #ccc;border-radius:4px}
.keyword-input,.section-select{top:583px;height:25px;background:#e3e3e3;border-radius:3px;font-size:8px;color:#333;line-height:25px;padding-left:8px}
.search-submit{left:410px;top:583px;width:86px;height:25px;border-radius:5px;background:linear-gradient(#ffc96b,#f59a1a);border:1px solid #d07800;font-size:12px;color:#333;text-align:center;line-height:23px}

/* info text */
.body-copy{width:452px;font-size:8.6px;line-height:11.2px;color:#222}

/* sidebar */
.browse-header{left:516px;top:392px;width:197px;height:29px;border-radius:5px;background:linear-gradient(#ffcf5a,#f39a12);font-size:12px;font-weight:600;color:#5a1800;text-align:center;line-height:29px;box-shadow:0 2px 3px rgba(0,0,0,.2)}
.browse-item{left:516px;width:197px;height:33px;background:linear-gradient(#fff 55%,#eeeeee);font-size:10.5px;color:#222;line-height:33px;padding-left:58px}
.browse-item::before{content:"";position:absolute;left:26px;top:13px;border-left:6px solid var(--orange);border-top:4px solid transparent;border-bottom:4px solid transparent}

.sell-panel{left:520px;top:697px;width:198px;height:143px;border-radius:6px;background:linear-gradient(#fdfdfd,#dedede);border:1px solid #c9c9c9}
.sell-title{left:546px;top:704px;font-size:17px;line-height:22px;color:var(--red)}
.learn-more{left:521px;top:768px;width:14px;height:56px;background:#7ab8e8;color:#234;font-size:8px;writing-mode:vertical-rl;transform:rotate(180deg);text-align:center;line-height:14px}
.seller-line{font-size:8.8px;line-height:11.5px;color:#222}

.dining-ad{left:521px;top:850px;width:197px;height:163px;background:#1a4a4f}
.dining-photo{left:611px;top:850px;width:107px;height:135px;background:radial-gradient(circle at 55% 55%,#8db86a,#3e7a5f 45%,#1a4a4f 80%)}
.ad-title{left:529px;top:856px;font-family:"Playfair Display",Georgia,serif;font-size:19px;line-height:19px;color:#fff}
.ad-title small{font-size:13px}
.ad-text{left:529px;top:902px;width:86px;font-size:8px;line-height:10.5px;color:#fff;font-weight:600}
.ad-strip{left:521px;top:986px;width:197px;height:27px;background:#fff;border:1px solid #ddd}
.ad-brand{left:527px;top:990px;font-size:15px;color:#d8232a}
.ad-button{left:641px;top:990px;width:71px;height:19px;background:#d8232a;border-radius:2px;color:#fff;font-size:8.5px;font-weight:700;text-align:center;line-height:19px}

/* footer */
.site-footer{left:8px;top:1028px;width:734px;height:137px;background:var(--footer);border-radius:8px}
.footer-heading{top:1046px;font-size:12.5px;color:var(--footer-head)}
.footer-link{font-size:9.5px;color:#fff}
.copyright{left:24px;top:1175px;font-size:8px;color:var(--red)}
.social-dot{top:1179px;width:17px;height:17px;border-radius:50%;background:radial-gradient(circle at 40% 35%,#4d86c9,#1b4f8f)}
</style>
</head>
<body>

<header>
  <div class="abs top-bar"></div>
  <div class="abs search-field">Search</div>
  <div class="abs go-button">GO</div>
  <div class="abs brand-name">periodicalbazaar.co.uk</div>
  <div class="abs phone-icon"><svg width="28" height="28" viewBox="0 0 28 28"><path d="M9 10c0-2 2-3 3-3l1 3-2 1c1 2 3 4 5 5l1-2 3 1c0 1-1 3-3 3-5 0-8-4-8-8z" fill="#fff"/></svg></div>
  <div class="abs phone-number">01555 204917</div>
  <div class="abs account-links"><span>Hello Guest</span><span>Login</span><span>My Basket (0)</span><span>Check out</span></div>
</header>

<nav>
  <div class="abs main-nav"></div>
  <div class="abs nav-item active">Home</div>
  <div class="abs nav-item" style="left:190px;width:40px">Buy</div>
  <div class="abs nav-item" style="left:265px;width:40px">Sell</div>
  <div class="abs nav-item" style="left:340px;width:60px">My Mags</div>
  <div class="abs nav-item" style="left:430px;width:50px">Help</div>
  <div class="abs nav-item" style="left:512px;width:90px">All Magazines</div>
</nav>

<section class="hero-banner">
  <div class="abs hero"></div>
  <div class="abs hero-covers" role="img" aria-label="Fanned stack of bridal and wedding magazine covers"></div>
  <div class="abs hero-title-small">Periodical</div>
  <div class="abs hero-title-large">Bazaar</div>
  <p class="abs hero-text">Contrary to popular belief, Lorem Ipsum is not simply random text. It has roots</p>
  <div class="abs hero-shadow"></div>
  <svg class="abs slide-arrow" style="left:24px" viewBox="0 0 30 42"><path d="M24 3 L6 21 L24 39" fill="none" stroke="#777" stroke-width="7" stroke-linecap="round" stroke-linejoin="round"/></svg>
  <svg class="abs slide-arrow" style="left:694px" viewBox="0 0 30 42"><path d="M6 3 L24 21 L6 39" fill="none" stroke="#777" stroke-width="7" stroke-linecap="round" stroke-linejoin="round"/></svg>
</section>

<main>
  <h1 class="abs section-heading" style="left:40px;top:385px">Welcome to Periodical Bazaar</h1>
  <div class="abs welcome-panel"></div>
  <div class="abs welcome-intro">Using this website you can...</div>
  <svg class="abs new-ribbon" viewBox="0 0 66 34"><path d="M10 0 H34 L66 28 V34 Z" fill="#f5c518"/><text x="31" y="12" font-size="7" font-weight="700" font-family="Open Sans,sans-serif" fill="#5a3a00" transform="rotate(38 31 12)">NEW</text></svg>
  <div class="abs action-button primary" style="left:58px">Search</div>
  <div class="abs action-button" style="left:167px">Buy</div>
  <div class="abs action-button" style="left:277px">Sell</div>
  <div class="abs action-button" style="left:386px">Read</div>
  <div class="abs action-caption" style="left:55px">For Article</div>
  <div class="abs action-caption" style="left:167px">Back issues</div>
  <div class="abs action-caption" style="left:277px">Your Magazines</div>
  <div class="abs action-caption" style="left:386px">Issues Online</div>

  <div class="abs search-panel"></div>
  <h2 class="abs section-heading" style="left:40px;top:555px">Article Search</h2>
  <div class="abs keyword-input" style="left:39px;width:177px">Keywords.....</div>
  <div class="abs section-select" style="left:225px;width:176px">All sections<svg style="position:absolute;right:10px;top:9px" width="8" height="6"><path d="M0 0H8L4 6Z" fill="#333"/></svg></div>
  <div class="abs search-submit">Search</div>

  <h2 class="abs section-heading" style="left:37px;top:648px">Back Issue Hobby Magazines</h2>
  <p class="abs body-copy" style="left:38px;top:676px">Periodical Bazaar sells back-issue magazines covering hobby subjects including Automotive, Aviation, Railway, Modelling, Motorbiking, Boating, Cycling and Men’s Lifestyle. Each section on our website contains dozens of magazine titles from different publishers. Use the left menu to start browsing our site…or alternatively use the...</p>

  <h2 class="abs section-heading" style="left:36px;top:733px">Magazine Article Search Facility</h2>
  <p class="abs body-copy" style="left:36px;top:761px">Use the Search facility (in the horizontal black bar above) to find magazine issues containing articles on specific topics. To improve relevance you can filter your search by Section (if searching from this page), or by Category or Title (if searching from within a Section)</p>

  <h2 class="abs section-heading" style="left:34px;top:808px">About Us – Buy Old Magazines Online</h2>
  <p class="abs body-copy" style="left:34px;top:836px">Periodical Bazaar is UK-based, and is an independent company offering magazines from many different publishers. At the heart of our service is a unique database of magazine issues &amp; articles covering thousands of titles stretching back to the 1950s. As well as listing our own large stocks, this website allows other private &amp; trade sellers to offer their old magazines for sale. Magazine back issues – and in some cases current issues &amp; subscriptions too – may be ordered from this site for mail-order delivery around the world</p>

  <h2 class="abs section-heading" style="left:32px;top:903px">Sell Your Magazines</h2>
  <p class="abs body-copy" style="left:32px;top:931px">Use this website to sell your old magazine collection for cash - click the button in the yellow box above for more information</p>

  <h2 class="abs section-heading" style="left:30px;top:963px">Magazine Subscriptions &amp; Digital Issues</h2>
  <p class="abs body-copy" style="left:30px;top:991px;width:470px">Subscriptions for many magazine titles may be purchased through this website, for yourself or as an ideal gift. In some cases individual magazine issues may also be downloaded in digital form.</p>
</main>

<aside>
  <div class="abs browse-header">Browse main sections</div>
  <div class="abs browse-item" style="top:422px">Aviation</div>
  <div class="abs browse-item" style="top:455px">Automotive</div>
  <div class="abs browse-item" style="top:488px">Railway</div>
  <div class="abs browse-item" style="top:521px">Cycling</div>
  <div class="abs browse-item" style="top:554px">Boating</div>
  <div class="abs browse-item" style="top:587px">Modelling</div>
  <div class="abs browse-item" style="top:620px">Men's lifestyle</div>
  <div class="abs browse-item" style="top:653px">Motorcycling</div>

  <div class="abs sell-panel"></div>
  <div class="abs sell-title">Sell your magazine<br>on this website</div>
  <div class="abs learn-more">Learn more</div>
  <div class="abs seller-line" style="left:546px;top:761px">Private Sellers..sell&nbsp;&nbsp;:&nbsp; Back Issues</div>
  <div class="abs seller-line" style="left:546px;top:784px">Trade Sellers..sell&nbsp;&nbsp;&nbsp;&nbsp;:</div>
  <div class="abs seller-line" style="left:631px;top:784px">Back Issues<br>Current Issues<br>Digital Issues<br>Subscriptions</div>

  <div class="abs dining-ad"></div>
  <div class="abs dining-photo" role="img" aria-label="Plated gourmet starter with garnish"></div>
  <div class="abs ad-title">Fine dining,<br><small>that’s affordable.</small></div>
  <div class="abs ad-text">Exclusive offers on restaurants with upto 70% off.</div>
  <div class="abs ad-strip"></div>
  <div class="abs ad-brand">tablewise</div>
  <div class="abs ad-button">Save upto 70%</div>
</aside>

<footer>
  <div class="abs site-footer"></div>
  <div class="abs footer-heading" style="left:39px">ABOUT US</div>
  <div class="abs footer-heading" style="left:139px">BUYING MAGAZINES</div>
  <div class="abs footer-heading" style="left:283px">SELLING MAGAZINES</div>
  <div class="abs footer-heading" style="left:433px">ADVERTISING</div>
  <div class="abs footer-heading" style="left:557px">CONTACT US</div>

  <div class="abs footer-link" style="left:39px;top:1071px">Who We Are</div>
  <div class="abs footer-link" style="left:39px;top:1093px">Our Service</div>
  <div class="abs footer-link" style="left:39px;top:1115px">Careers</div>
  <div class="abs footer-link" style="left:39px;top:1138px">Contact us</div>

  <div class="abs footer-link" style="left:139px;top:1071px">Buying Back Issues</div>
  <div class="abs footer-link" style="left:139px;top:1093px">Buying Subscriptions</div>
  <div class="abs footer-link" style="left:139px;top:1115px">Buying FAQ's</div>

  <div class="abs footer-link" style="left:283px;top:1071px">New Seller Overview</div>
  <div class="abs footer-link" style="left:283px;top:1093px">Seller Terms &amp; Conditions</div>
  <div class="abs footer-link" style="left:283px;top:1115px">Publisher Services</div>
  <div class="abs footer-link" style="left:283px;top:1138px">Register / Log-In</div>

  <div class="abs footer-link" style="left:433px;top:1069px">Advertising Overview</div>
  <div class="abs footer-link" style="left:433px;top:1091px">Rate Card</div>
  <div class="abs footer-link" style="left:433px;top:1114px">Make Booking</div>

  <div class="abs footer-link" style="left:559px;top:1066px;font-size:9px">Periodical Bazaar, 18 Kiln Lane,</div>
  <div class="abs footer-link" style="left:559px;top:1089px;font-size:9px">Westbrook, Lowshire,</div>
  <div class="abs footer-link" style="left:559px;top:1112px;font-size:9px">LW4 7QT, UK.</div>
  <div class="abs footer-link" style="left:559px;top:1134px;font-size:9px">Email:&nbsp; orders@periodicalbazaar.co.uk</div>

  <div class="abs copyright">Copyright © 2011. www.periodicalbazaar.co.uk</div>
  <div class="abs social-dot" style="left:663px"></div>
  <div class="abs social-dot" style="left:682px"></div>
  <div class="abs social-dot" style="left:701px"></div>
</footer>

</body>
</html>
```